Personal Training Studio needs small flyer design

My Personal Training Studio is looking to offer local high end clothes shops the option to offer their customers free Personal Training at our studio. It will be a small flyer (more a slip - landscape) that can be put into customers shopping bags once they have purchased an item from the store.
It is being marketed as a Local Fitness Initiative which is called "Be Fit In Your Clothes" The idea is to come from a "Be Fit" health perspective but also "Fit into your clothes" from the clothes shops perspective. Perhaps the "Be" in a different colour to the rest of the title. I would like my company logo and colours to be used, plus the address of the of the studio (see website - www.harbourlane7gym.co.uk). Flyer can be double sided

Target Market(s)

High end clothing shops

Industry/Entity Type

Training

Requirements
Must have
• Reference to the fact that the voucher is offering a FREE Personal Training session. Contact us to book yours today.

```html
<!DOCTYPE html>
<html lang="en">
<head>
<meta charset="utf-8">
<title>Be Fit In Your Clothes – Flyer</title>
<link rel="stylesheet" href="https://fonts.googleapis.com/css2?family=Rubik+Dirt&family=Open+Sans:wght@400;600&display=swap">
<style>
  :root {
    --page: #e9e7e3;
    --slate: #3f5561;
    --navy: #2a3670;
    --navy-deep: #232d63;
    --sky: #3c9fc9;
    --teal: #2f86a6;
    --grey-bar: #6f7c83;
    --circle: #8a979d;
    --band-top: #d7dadc;
    --band-bottom: #aeb5b9;
    --white: #ffffff;
    --ink: #1f2a66;
    --personal: #9fd6ea;
  }
  html, body {
    margin: 0;
    width: 1200px;
    height: 1000px;
    overflow: hidden;
    background: var(--page);
  }
  .flyer {
    position: absolute;
    left: 90px;
    top: 190px;
    width: 1020px;
    height: 620px;
    background: var(--slate);
    overflow: hidden;
    box-shadow: 0 6px 24px rgba(0,0,0,0.18);
  }
  .flyer__shapes { position: absolute; inset: 0; }
  .photo { position: absolute; }
  .photo--trainer-left {
    left: 30px; top: 310px; width: 280px; height: 170px;
    background: linear-gradient(160deg, #5b4f83, #3a3a6e 70%);
    opacity: 0.85;
  }
  .photo--arm-dumbbell {
    left: 310px; top: 390px; width: 420px; height: 90px;
    background: linear-gradient(90deg, #3a4a55, #55636b 60%, #3e4e58);
  }
  .photo--model-right {
    left: 800px; top: 0; width: 220px; height: 250px;
    background: linear-gradient(180deg, #b98a73 0%, #c4d65a 45%, #2e2e36 100%);
  }
  .headline {
    position: absolute;
    inset: 0;
    margin: 0;
    font-family: "Rubik Dirt", "Arial Black", sans-serif;
    font-weight: 400;
    color: var(--white);
    line-height: 1;
    white-space: nowrap;
  }
  .headline__be {
    position: absolute;
    left: 50px; top: 115px;
    font-size: 160px;
    color: var(--sky);
  }
  .headline__line {
    position: absolute;
    left: 295px;
    font-size: 60px;
  }
  .headline__line--first { top: 120px; }
  .headline__line--second { top: 188px; }
  .offer {
    position: absolute;
    left: 520px; top: 268px;
    font-family: "Open Sans", Arial, sans-serif;
    color: var(--white);
    white-space: nowrap;
  }
  .offer__top {
    display: inline-flex; align-items: flex-end;
    background: var(--navy-deep);
  }
  .offer__free {
    background: var(--teal);
    font-weight: 600;
    font-size: 48px;
    line-height: 1;
    padding: 4px 10px 6px;
  }
  .offer__personal {
    font-size: 24px;
    padding: 0 12px 6px 8px;
    color: var(--personal);
  }
  .offer__bottom {
    background: var(--grey-bar);
    font-size: 24px;
    padding: 3px 12px 5px;
    color: #e4e8ea;
  }
  .brand {
    position: absolute;
    left: 820px; top: 250px;
    width: 200px; height: 130px;
    background: var(--navy);
    display: flex; align-items: center; justify-content: center;
  }
  .brand__name {
    font-family: "Open Sans", Arial, sans-serif;
    font-weight: 400;
    font-size: 20px;
    letter-spacing: 1px;
    line-height: 1.25;
    color: var(--white);
    text-align: center;
  }
  .brand__line { display: block; }
  .contact {
    position: absolute;
    left: 0; right: 0; bottom: 0;
    height: 140px;
    background: linear-gradient(180deg, var(--band-top), var(--band-bottom));
    font-family: "Open Sans", Arial, sans-serif;
    color: var(--ink);
    padding: 20px 0 0 140px;
    box-sizing: border-box;
    white-space: nowrap;
  }
  .contact__phones { font-size: 46px; line-height: 1.1; }
  .contact__address { font-size: 24px; font-weight: 600; }
</style>
</head>
<body>
  <section class="flyer">
    <svg class="flyer__shapes" width="1020" height="620" viewBox="0 0 1020 620" aria-hidden="true">
      <polygon points="0,0 430,0 760,620 0,620" fill="var(--navy)" opacity="0.9"/>
      <circle cx="640" cy="80" r="60" fill="var(--navy)" opacity="0.6"/>
      <circle cx="730" cy="160" r="62" fill="var(--circle)" opacity="0.7"/>
      <circle cx="800" cy="50" r="75" fill="#5a5f92" opacity="0.7"/>
    </svg>

    <div class="photo photo--trainer-left" role="img" aria-label="Photo of a woman training, tinted purple"></div>
    <div class="photo photo--arm-dumbbell" role="img" aria-label="Photo of an arm lifting a dumbbell"></div>
    <div class="photo photo--model-right" role="img" aria-label="Photo of a smiling woman in a lime sports top holding a pink dumbbell"></div>

    <h1 class="headline">
      <span class="headline__be">Be</span>
      <span class="headline__line headline__line--first">Fit In</span>
      <span class="headline__line headline__line--second">Your Clothes</span>
    </h1>

    <div class="offer">
      <div class="offer__top">
        <span class="offer__free">FREE</span>
        <span class="offer__personal">Personal</span>
      </div>
      <div class="offer__bottom">Training at our studio</div>
    </div>

    <div class="brand">
      <span class="brand__name">
        <span class="brand__line">HARBOURLANE7</span>
        <span class="brand__line">GYM</span>
      </span>
    </div>

    <div class="contact">
      <div class="contact__phones">01632 960418 • 07700 900274</div>
      <div class="contact__address">7 Harbour Lane, Eastmoor, North Yorkshire EM4 2TX</div>
    </div>
  </section>
</body>
</html>
```